Staff Newsletter Template Image

We are looking for two .jpg images that we can put into a Word document and use for our staff newsletter. We will then add content using text boxes.
Attached is the current template which works for the columns and size that we need but we just want a fresh new design.
The Word document shows how we use it.
The name will stay the same - Team upBeat but can be a different look to the current one.

Target Market(s)

Sales team

Colors

Designer to choose colors to be used in the design.

Requirements
Must have
• Colours will be green, grey and white, possibly cream if needed. All from the guidelines.
• I have attached our brand guidelines which shows design elements and fonts for our brand. Also attached is brand guidelines for one of our product lines as we would like to use the same green.
• It needs to be nice to look at and motivational for our team

```html
<!DOCTYPE html>
<html lang="en">
<head>
<meta charset="utf-8">
<title>Team upBeat – Staff Newsletter</title>
<link rel="stylesheet" href="https://fonts.googleapis.com/css2?family=Open+Sans:wght@400;700;800&display=swap">
<style>
  :root {
    --green: #66c00b;
    --green-soft: #7dbf35;
    --charcoal: #2b2b2d;
    --rule-grey: #9a9ca6;
    --white: #ffffff;
    --table-head: #7cbf30;
    --table-row-a: #99bd6a;
    --table-row-b: #8cbd52;
    --ink: #1e1e1e;
  }
  * { margin: 0; padding: 0; box-sizing: border-box; }
  html, body { width: 1200px; height: 846px; overflow: hidden; background: var(--white); }
  body { font-family: "Open Sans", Arial, sans-serif; color: var(--ink); }
  .canvas { position: relative; width: 1200px; height: 846px; overflow: hidden; background: var(--white); }
  .shapes { position: absolute; left: 0; top: 0; }
  .abs { position: absolute; }

  .masthead-name {
    left: 36px; top: 60px;
    font-size: 50px; font-weight: 700; letter-spacing: 0.5px;
    color: var(--charcoal); line-height: 1;
  }
  .issue-date { left: 400px; width: 169px; top: 177px; text-align: right; font-size: 9.6px; color: var(--white); }
  .greeting { left: 34px; top: 223px; font-size: 9.4px; }

  .panel-dark { color: var(--white); }
  h2 { font-weight: 700; line-height: 1.2; }
  .h-dark { font-size: 14.6px; color: var(--white); }
  .h-ink { font-size: 14.6px; color: var(--charcoal); }

  .sellers { left: 324px; top: 231px; width: 245px; }
  .sellers .intro { font-size: 9.6px; line-height: 15px; text-align: justify; margin-top: 5px; }
  .sellers .basis { font-size: 8.6px; text-decoration: underline; margin-top: 1px; }

  .rank-table { left: 324px; top: 312px; width: 245px; border-collapse: collapse; font-size: 9.6px; color: var(--ink); }
  .rank-table th, .rank-table td { height: 19px; padding: 0; }
  .rank-table th { background: var(--table-head); font-weight: 700; }
  .rank-table tr:nth-child(odd) td { background: var(--table-row-a); }
  .rank-table tr:nth-child(even) td { background: var(--table-row-b); }
  .rank-table .col-rank { width: 42px; text-align: center; border-right: 1px solid rgba(255,255,255,0.35); }
  .rank-table .col-member { text-align: left; padding-left: 19px; }

  .tip-list { list-style: none; font-size: 8.6px; line-height: 19.7px; text-align: justify; }
  .tip-list li { text-indent: 6px; }
  .tip-list svg { width: 8px; height: 8px; vertical-align: -1px; margin-right: 2px; }
  .on-dark { color: var(--white); }
  .on-dark svg { color: var(--green-soft); }
  .on-light svg { color: var(--charcoal); }

  .top-tip { left: 324px; top: 404px; width: 249px; }
  .top-tip .tip-list { margin-top: 10px; }
  .shout { left: 324px; top: 657px; width: 245px; }
  .shout p { font-size: 9.6px; line-height: 15px; margin-top: 3px; }
  .shout p + p { margin-top: 0; }

  .tips-green { left: 633px; top: 55px; width: 249px; color: var(--charcoal); }
  .tips-white { left: 920px; top: 55px; width: 249px; color: var(--charcoal); }
  .tips-green .tip-list, .tips-white .tip-list { margin-top: 5px; }

  .reminders { left: 633px; top: 543px; width: 249px; }
  .reminders p, .member-means p { font-size: 8.6px; line-height: 19.7px; text-align: justify; }
  .reminders h2 { margin-bottom: 2px; }

  .member-means { left: 920px; top: 665px; width: 249px; color: var(--white); }
  .member-means h2 { font-size: 14.6px; line-height: 22px; margin-bottom: 4px; }
</style>
</head>
<body>
<div class="canvas">
  <svg class="shapes" width="1200" height="846" viewBox="0 0 1200 846" aria-hidden="true">
    <defs>
      <linearGradient id="greenFade" x1="0" y1="0" x2="0" y2="1">
        <stop offset="0" stop-color="#63c00a"/>
        <stop offset="1" stop-color="#7dbf35"/>
      </linearGradient>
      <symbol id="arrow-badge" viewBox="0 0 16 16">
        <circle cx="8" cy="8" r="8" fill="currentColor"/>
        <path d="M4 7h5V4.5L12.5 8 9 11.5V9H4z" fill="#2b2b2d"/>
      </symbol>
      <symbol id="arrow-badge-light" viewBox="0 0 16 16">
        <circle cx="8" cy="8" r="8" fill="currentColor"/>
        <path d="M4 7h5V4.5L12.5 8 9 11.5V9H4z" fill="#6fbf1e"/>
      </symbol>
      <symbol id="arrow-badge-white" viewBox="0 0 16 16">
        <circle cx="8" cy="8" r="8" fill="currentColor"/>
        <path d="M4 7h5V4.5L12.5 8 9 11.5V9H4z" fill="#ffffff"/>
      </symbol>
    </defs>
    <!-- front page header bands -->
    <polygon points="18,145 125,145 18,191" fill="url(#greenFade)"/>
    <polygon points="29,196 144,145 328,145 209,196" fill="url(#greenFade)"/>
    <polygon points="232,196 593,37 593,196" fill="url(#greenFade)"/>
    <!-- front page body -->
    <rect x="305" y="196" width="288" height="627" fill="var(--charcoal)"/>
    <polygon points="18,779 305,652 305,823 18,823" fill="url(#greenFade)"/>
    <rect x="18" y="823" width="575" height="6" fill="var(--rule-grey)"/>
    <!-- inside page -->
    <rect x="607" y="17" width="301" height="801" fill="url(#greenFade)"/>
    <polygon points="908,644 1181,557 1181,818 908,818" fill="var(--charcoal)"/>
    <rect x="607" y="818" width="574" height="11" fill="var(--rule-grey)"/>
  </svg>

  <div class="abs masthead-name">Team upBeat</div>
  <div class="abs issue-date">Date: 14 - 12 -2019</div>
  <p class="abs greeting">Hi everyone,</p>

  <section class="abs sellers panel-dark">
    <h2 class="h-dark">Top Sellers!</h2>
    <p class="intro">The following upBeat team members were our top sellers last week</p>
    <p class="basis">Based on completed sales</p>
  </section>

  <table class="abs rank-table">
    <thead>
      <tr><th class="col-rank">#</th><th class="col-member">Team Member</th></tr>
    </thead>
    <tbody>
      <tr><td class="col-rank">1</td><td class="col-member">- 100 upBeat Dollars</td></tr>
      <tr><td class="col-rank">2</td><td class="col-member">- 50 upBeat Dollars</td></tr>
      <tr><td class="col-rank">3</td><td class="col-member">- 25 upBeat Dollars</td></tr>
    </tbody>
  </table>

  <section class="abs top-tip">
    <h2 class="h-dark">Top Tip from our Week’s Top Seller</h2>
    <ul class="tip-list on-dark">
      <li><svg><use href="#arrow-badge"/></svg>Sed ut perspiciatis unde omnis iste natus error sit voluptatem accusantium doloremque laudantium</li>
      <li><svg><use href="#arrow-badge"/></svg>Sed ut perspiciatis unde omnis iste natus error sit voluptatem accusantium doloremque laudantium</li>
      <li><svg><use href="#arrow-badge"/></svg>Sed ut perspiciatis unde omnis iste natus error sit voluptatem accusantium doloremque laudantium</li>
      <li><svg><use href="#arrow-badge"/></svg>Sed ut perspiciatis unde omnis iste natus error sit voluptatem accusantium doloremque laudantium</li>
      <li><svg><use href="#arrow-badge"/></svg>Sed ut perspiciatis unde omnis iste natus error sit voluptatem accusantium doloremque laudantium</li>
    </ul>
  </section>

  <section class="abs shout panel-dark">
    <h2 class="h-dark">Shout Out</h2>
    <p>Name</p>
    <p>[Comments]</p>
  </section>

  <section class="abs tips-green">
    <h2 class="h-ink">Tips &amp; Hints</h2>
    <ul class="tip-list on-light">
      <li><svg><use href="#arrow-badge-light"/></svg>Sed ut perspiciatis unde omnis iste natus error sit voluptatem accusantium doloremque laudantium</li>
      <li><svg><use href="#arrow-badge-light"/></svg>Sed ut perspiciatis unde omnis iste natus error sit voluptatem accusantium doloremque laudantium</li>
      <li><svg><use href="#arrow-badge-light"/></svg>Sed ut perspiciatis unde omnis iste natus error sit voluptatem accusantium doloremque laudantium</li>
      <li><svg><use href="#arrow-badge-light"/></svg>Sed ut perspiciatis unde omnis iste natus error sit voluptatem accusantium doloremque laudantium</li>
      <li><svg><use href="#arrow-badge-light"/></svg>Sed ut perspiciatis unde omnis iste natus error sit voluptatem accusantium doloremque laudantium</li>
      <li><svg><use href="#arrow-badge-light"/></svg>Sed ut perspiciatis unde omnis iste natus error sit voluptatem accusantium doloremque laudantium</li>
      <li><svg><use href="#arrow-badge-light"/></svg>Sed ut perspiciatis unde omnis iste natus error sit voluptatem accusantium doloremque laudantium</li>
      <li><svg><use href="#arrow-badge-light"/></svg>Sed ut perspiciatis unde omnis iste natus error sit voluptatem accusantium doloremque laudantium</li>
      <li><svg><use href="#arrow-badge-light"/></svg>Sed ut perspiciatis unde omnis iste natus error sit voluptatem accusantium doloremque laudantium</li>
      <li><svg><use href="#arrow-badge-light"/></svg>Sed ut perspiciatis unde omnis iste natus error sit voluptatem accusantium doloremque laudantium</li>
      <li><svg><use href="#arrow-badge-light"/></svg>Sed ut perspiciatis unde omnis iste natus error sit voluptatem accusantium doloremque laudantium</li>
    </ul>
  </section>

  <section class="abs tips-white">
    <h2 class="h-ink">Tips &amp; Hints</h2>
    <ul class="tip-list on-light">
      <li><svg><use href="#arrow-badge-white"/></svg>Sed ut perspiciatis unde omnis iste natus error sit voluptatem accusantium doloremque laudantium</li>
      <li><svg><use href="#arrow-badge-white"/></svg>Sed ut perspiciatis unde omnis iste natus error sit voluptatem accusantium doloremque laudantium</li>
      <li><svg><use href="#arrow-badge-white"/></svg>Sed ut perspiciatis unde omnis iste natus error sit voluptatem accusantium doloremque laudantium</li>
      <li><svg><use href="#arrow-badge-white"/></svg>Sed ut perspiciatis unde omnis iste natus error sit voluptatem accusantium doloremque laudantium</li>
      <li><svg><use href="#arrow-badge-white"/></svg>Sed ut perspiciatis unde omnis iste natus error sit voluptatem accusantium doloremque laudantium</li>
      <li><svg><use href="#arrow-badge-white"/></svg>Sed ut perspiciatis unde omnis iste natus error sit voluptatem accusantium doloremque laudantium</li>
      <li><svg><use href="#arrow-badge-white"/></svg>Sed ut perspiciatis unde omnis iste natus error sit voluptatem accusantium doloremque laudantium</li>
      <li><svg><use href="#arrow-badge-white"/></svg>Sed ut perspiciatis unde omnis iste natus error sit voluptatem accusantium doloremque laudantium</li>
      <li><svg><use href="#arrow-badge-white"/></svg>Sed ut perspiciatis unde omnis iste natus error sit voluptatem accusantium doloremque laudantium</li>
      <li><svg><use href="#arrow-badge-white"/></svg>Sed ut perspiciatis unde omnis iste natus error sit voluptatem accusantium doloremque laudantium</li>
      <li><svg><use href="#arrow-badge-white"/></svg>Sed ut perspiciatis unde omnis iste natus error sit voluptatem accusantium doloremque laudantium</li>
    </ul>
  </section>

  <section class="abs reminders">
    <h2 class="h-ink">Reminders</h2>
    <p>Lorem ipsum dolor sit amet, consectetur adipiscing elit, sed do eiusmod tempor incididunt ut labore et dolore magna aliqua. Quis ipsum suspendisse ultrices gravida. Risus commodo viverra maecenas accumsan lacus vel facilisis.</p>
    <p>Lorem ipsum dolor sit amet, consectetur adipiscing elit, sed do eiusmod tempor incididunt ut labore et dolore magna aliqua. Risus commodo viverra maecenas accumsan lacus vel facilisis.</p>
    <p>Lorem ipsum dolor sit amet, consectetur adipiscing elit, sed do eiusmod tempor incididunt ut labore et dolore magna aliqua. Quis ipsum suspendisse ultrices gravida.</p>
  </section>

  <section class="abs member-means">
    <h2>Being an upBeat Team Member Means...</h2>
    <p>Lorem ipsum dolor sit amet, consectetur adipiscing elit, sed do eiusmod tempor incididunt ut labore et dolore magna aliqua. Quis ipsum suspendisse ultrices gravida. Risus commodo viverra maecenas accumsan lacus vel facilisis.</p>
  </section>
</div>
</body>
</html>
```